Lumen Thread Business Card Design

Lumen Thread is a platform that allows advertisers and their agencies to build media plans across millions of influencers that support their objectives. Once the media plan is approved, it allows you collaborate with influencers, approve creative direction and distribute content across over 20 channels, all while ensuring it is measured and in line with your guidelines.

We are looking for a designer to help us create one of the most unique business cards you have ever received. In summary, we are looking for one side of our business card design to incorporate our logo and contact details and the second side to incorporate what we do, show different social media images.

Size : See attachment for size guidelines. Square Business Card Template.

Logo : See attached.

Front :
Logo : Lumen Thread (attached)
Name: Marisol Bekker
Job Title: Co - Founder
Phone Number : Au +61 400 583 917
Email : marisol.bekker@lumenthread.com
Web : lumenthread.com

Back :
We would like to see 3 versions for the back.

Back One
Pictora Picture : See attached Full Size Render 5
lumen thread Logo : Somehow watermarked over the picture in a subtle way
Copy : Pictora Logo @marisolbek8 / Genre - Fashion

Back Two
Kinbridge Picture : See attached Full Size Render 4
Copy : Kinbridge Logo @marisolbek8 / Genre - Travel

Back Three
Chirpline Copy : "Toasting to exciting adventures in my gorgeous new dress and dancing shoes. Here’s to a glitzy and dazzling 2015!"
Copy : Chirpline Logo @marisolbek8 / Genre - Business

Note : Social Media Logos attached

Target Market(s)

See Project Description

Industry/Entity Type

Business

Contact Information for Business Card

See Project Description

Font styles to use
Other font styles liked:
• See Logo

Colors
1696d0
33a6d7
85cae6
0355a3
ec1f27

Requirements
Must have
• See Project Description
Nice to have
• See Project Description
Should not have
• See Project Description

```html
<!DOCTYPE html>
<html lang="en">
<head>
<meta charset="utf-8">
<title>Lumen Thread — Business Card</title>
<link rel="stylesheet" href="https://fonts.googleapis.com/css2?family=PT+Sans+Narrow:wght@400;700&family=Source+Sans+3:wght@400;600&family=Arimo:wght@400&display=swap">
<style>
  :root {
    --backdrop: #eceef1;
    --card: #ffffff;
    --brand-navy: #0355a3;
    --brand-sky: #33a6d7;
    --brand-sky-bright: #29a8e0;
    --title-ink: #1b3556;
    --body-ink: #3a3a3a;
    --icon-navy: #1d4f8c;
    --band-deep: #1f6dbb;
    --band-glow: #2fb0e6;
    --band-edge: #8fd0ee;
  }
  * { box-sizing: border-box; margin: 0; padding: 0; }
  html, body {
    width: 1200px; height: 1153px; overflow: hidden;
    background: var(--backdrop);
  }
  .card {
    position: absolute; left: 150px; top: 126px;
    width: 900px; height: 900px;
    background: var(--card);
    box-shadow: 0 6px 24px rgba(0,0,0,.12);
    overflow: hidden;
  }
  .brand {
    position: absolute; left: 54px; top: 74px;
    display: flex; align-items: center; gap: 24px;
  }
  .brand-mark {
    width: 112px; height: 112px; border-radius: 14px;
    background: var(--brand-navy);
  }
  .brand-name {
    font-family: "Source Sans 3", sans-serif; font-weight: 600;
    color: var(--brand-navy);
    font-size: 70px; line-height: 58px; letter-spacing: -1px;
  }
  .person { position: absolute; left: 52px; top: 302px; }
  .person-name {
    font-family: "PT Sans Narrow", sans-serif; font-weight: 700;
    font-size: 74px; line-height: 80px; color: var(--brand-sky-bright);
  }
  .person-role {
    font-family: "PT Sans Narrow", sans-serif; font-weight: 700;
    font-size: 58px; line-height: 62px; color: var(--title-ink);
  }
  .contacts { position: absolute; left: 54px; top: 476px; list-style: none; }
  .contact {
    display: flex; align-items: center; gap: 16px;
    height: 59px;
    font-family: "Arimo", sans-serif; font-size: 36px; color: var(--body-ink);
  }
  .contact--address { font-family: "Source Sans 3", sans-serif; font-size: 38px; height: 64px; }
  .contact-icon { width: 36px; height: 36px; flex: none; }
  .band {
    position: absolute; left: 0; bottom: 0; width: 900px; height: 158px;
    border-top: 4px solid var(--band-edge);
    background:
      radial-gradient(ellipse 150px 110px at 270px 45%, var(--band-glow), rgba(47,176,230,0) 100%),
      var(--band-deep);
  }
</style>
</head>
<body>
  <div class="card">
    <div class="brand">
      <div class="brand-mark"></div>
      <div class="brand-name">lumen<br>thread</div>
    </div>

    <div class="person">
      <div class="person-name">Marisol Bekker</div>
      <div class="person-role">Co - Founder</div>
    </div>

    <ul class="contacts">
      <li class="contact contact--address">
        <svg class="contact-icon" viewBox="0 0 36 36" aria-hidden="true">
          <circle cx="18" cy="18" r="17" fill="var(--icon-navy)"/>
          <path d="M9 18 L18 10 L27 18 M12 16 V26 H16 V20 H20 V26 H24 V16" fill="none" stroke="#fff" stroke-width="2.2" stroke-linejoin="round"/>
        </svg>
        Please Provide address
      </li>
      <li class="contact">
        <svg class="contact-icon" viewBox="0 0 36 36" aria-hidden="true">
          <circle cx="18" cy="18" r="17" fill="var(--icon-navy)"/>
          <path d="M12 9 C10 11 10 15 13 20 C16 25 20 28 24 28 L26 25 L22 22 L20 24 C18 23 15 19 14 16 L16 14 L14 9 Z" fill="#fff"/>
        </svg>
        Au +61 400 583 917
      </li>
      <li class="contact">
        <svg class="contact-icon" viewBox="0 0 36 36" aria-hidden="true">
          <circle cx="18" cy="18" r="17" fill="var(--icon-navy)"/>
          <text x="18" y="24" text-anchor="middle" font-family="Arial, sans-serif" font-size="18" font-weight="700" fill="#fff">@</text>
        </svg>
        marisol.bekker@lumenthread.com
      </li>
      <li class="contact">
        <svg class="contact-icon" viewBox="0 0 36 36" aria-hidden="true">
          <circle cx="18" cy="18" r="17" fill="var(--icon-navy)"/>
          <g fill="none" stroke="#fff" stroke-width="1.8">
            <circle cx="18" cy="18" r="9"/>
            <ellipse cx="18" cy="18" rx="4" ry="9"/>
            <path d="M9 18 H27"/>
          </g>
        </svg>
        lumenthread.com
      </li>
    </ul>

    <div class="band"></div>
  </div>
</body>
</html>
```